Web Design Project

I need designs (PSD only - no programming) for several pages of a new website helping train operators to manage key information about their traindrivers.
The main feature of this website is the management of personnel records (create, edit, search, delete). Another key aspect is the management of user privileges. Since this is a new website we also need a user friendly frontpage, pricing information and how it works sections.
This can be broken down into 9 pages for which we need designs (PSDs).
1. Home
2. Driver record
3. How it works
4. Pricing
5. User administration
6. Help
7. Record list view
8. Login
9. Registration
Navigation (not logged in) are: Home | How it works | Pricing | Customers | About us | Contact
Navigation (logged in) are: Overview | Administration | Manage records | Billing | Help | Contact
Footer: Customer logos | Awards | Terms & Conditions | Privacy
To provide the best support for you to come up with a strong design proposal I will provide DAILY feedback to all participants. We have also created concept mockups (attached) and example pages (below) for each section to give you a clear sense of what we look for.
The core concepts for a successful bid are that the website is EASY to understand, INTUITIVE to navigate, and SIMPLE to use. Most of our users lack technical background and are looking for tool to simplify their work.
The strongest participants (winner and close contenders) will have the opportunity to additional commissioned work on additional sections not included in this brief.
Example Pages (by section)
1. http://www.brovendale.example/site-keepers/
1. http://www.qvt.example/
1. http://www.mondaph.example/
1. http://www.gorvanquest.example/
2. http://www.snapveld.example/profile_edit.gne
3. https://www.tarn.example/how-it-works/
3. http://www.bulkvue.example/learn
4. http://www.pactheron.example/crm/editions-pricing.jsp
4. http://www.brovendale.example/site-keepers/prices
6. https://support.talvora.example/en-gb/
6. http://help.dealmeadow.example/contact_us
8. https://www.careweave.example/uas/login
8. https://www.dealmeadow.example/login
8. http://www.askhollow.example/login/index
For form designs we like Verindo, Bidnook, Snapveld, CareWeave, Chatterly and the concepts presented by Tomas Kerrigan in his classic Layout Craft Shaping the Input Boxes.
For additional guidance see mockups attached!
Target Market(s)
Security, human resources and admin support employees for train operators.
Industry/Entity Type
Learn
Requirements
Should not have
- Home page should not have
Social media icons (chatterly, chirpla, CareWeave, RSS feed)
Contact forms
Read more links
Old trains

```html
<!DOCTYPE html>
<html lang="en">
<head>
<meta charset="utf-8">
<title>RailRoster – Here to help</title>
<link rel="stylesheet" href="https://fonts.googleapis.com/css2?family=Didact+Gothic&family=Varela+Round&display=swap">
<style>
  :root {
    --page-bg: #ffffff;
    --navy: #1d4a6e;
    --nav-blue: #1f5582;
    --orange: #f39a2c;
    --brand-blue: #2fa9d9;
    --text: #4f4f4f;
    --text-dark: #2b2b2b;
    --muted: #9a9a9a;
    --rule: #dcdcdc;
    --panel-border: #d6d6d6;
    --button-top: #5cc3ec;
    --button-bottom: #2a9fd3;
    --logo-grey: #b9b9b9;
  }
  * { box-sizing: border-box; margin: 0; padding: 0; }
  html, body { width: 1200px; height: 799px; overflow: hidden; background: var(--page-bg); }
  body { position: relative; font-family: "Didact Gothic", "Varela Round", sans-serif; color: var(--text); }
  a { text-decoration: none; color: inherit; }

  .site-header {
    position: absolute; left: 0; top: 0; width: 1200px; height: 113px;
    background: linear-gradient(#ffffff 0, #ffffff 36px, #f1f1f1 70px, #d9d9d9 106px);
    border-bottom: 7px solid var(--orange);
  }
  .utility-nav { position: absolute; top: 14px; left: 893px; display: flex; gap: 18px; font-size: 12px; color: #333; }
  .brand { position: absolute; left: 132px; top: 44px; display: flex; align-items: center; gap: 8px;
    font-family: "Varela Round", sans-serif; font-size: 33px; color: var(--brand-blue); letter-spacing: -0.5px; }
  .main-nav { position: absolute; top: 55px; right: 147px; display: flex; gap: 36px;
    font-family: "Varela Round", sans-serif; font-size: 17.5px; color: var(--nav-blue); }

  .page-title { position: absolute; left: 128px; top: 140px; font-family: "Varela Round", sans-serif;
    font-size: 22px; color: var(--navy); font-weight: 700; }
  .title-rule { position: absolute; left: 128px; top: 173px; width: 942px; border-top: 1px solid var(--rule); }

  .help-panel {
    position: absolute; left: 188px; top: 204px; width: 824px; height: 358px;
    border: 2px solid #e4e4e4; border-radius: 4px;
    background: linear-gradient(#ffffff, #f7f7f7);
    box-shadow: 0 5px 0 -1px #cfcfcf, 0 2px 6px rgba(0,0,0,0.08);
  }
  .help-intro { position: absolute; left: 55px; top: 36px; width: 700px; font-size: 12.5px; line-height: 20.5px; color: var(--text); }
  .panel-divider { position: absolute; left: 490px; top: 112px; width: 14px; height: 224px;
    background: linear-gradient(90deg, rgba(0,0,0,0.06), rgba(0,0,0,0)); border-left: 1px solid #e2e2e2; }

  .question { position: absolute; left: 55px; top: 152px; width: 376px; }
  .question-heading { font-family: "Varela Round", sans-serif; font-size: 17px; color: var(--orange);
    padding-bottom: 12px; border-bottom: 1px solid var(--rule); }
  .search-form { display: flex; margin-top: 17px; height: 45px; }
  .search-field { flex: 1; display: flex; align-items: center; gap: 10px; padding-left: 10px;
    border: 2px solid #d8d8d8; border-right: none; background: #fbfbfb; font-size: 14.5px; color: #333; font-weight: 600; }
  .search-button { width: 90px; background: linear-gradient(var(--button-top), var(--button-bottom));
    color: #fff; font-family: "Varela Round", sans-serif; font-size: 15.5px; letter-spacing: 0.5px;
    display: flex; align-items: center; justify-content: center; border: 1px solid #2793c4; }

  .more-help { position: absolute; left: 550px; top: 152px; }
  .more-help-heading { font-family: "Varela Round", sans-serif; font-size: 17px; color: var(--text-dark); }
  .contact-line { display: flex; align-items: center; gap: 10px; margin-top: 18px; font-size: 15.5px; color: var(--text-dark); }
  .contact-line:first-of-type { margin-top: 20px; }
  .contact-line strong { color: var(--orange); font-weight: 700; }

  .partners-title { position: absolute; left: 130px; top: 618px; font-family: "Varela Round", sans-serif;
    font-size: 22px; color: var(--muted); font-weight: 700; }
  .partners-tab { position: absolute; left: 566px; top: 626px; width: 96px; height: 60px; border-radius: 48px 48px 0 0;
    background: linear-gradient(#f2f2f2, #ffffff 60%); }
  .partners-rule { position: absolute; left: 130px; top: 654px; width: 940px; border-top: 1px solid var(--rule); }
  .partner-row { position: absolute; left: 130px; top: 676px; width: 940px; height: 52px; }
  .partner-badge { position: absolute; top: 6px; width: 40px; height: 40px; background: var(--logo-grey); opacity: 0.75; }
  .partner-badge.round { border-radius: 50%; }
  .footer-rule { position: absolute; left: 130px; top: 748px; width: 940px; border-top: 1px solid var(--rule); }
  .site-footer { position: absolute; left: 130px; top: 766px; width: 940px; display: flex; justify-content: space-between;
    font-size: 12.5px; color: #777; }
  .site-footer .terms { color: var(--nav-blue); }
  .footer-nav span { margin: 0 5px; }
</style>
</head>
<body>
  <header class="site-header">
    <nav class="utility-nav"><a href="#">Sign Up</a><a href="#">Login</a><a href="#">Language</a></nav>
    <a class="brand" href="#">RailRoster</a>
    <nav class="main-nav">
      <a href="#">Home</a><a href="#">How it Works</a><a href="#">Prices</a>
      <a href="#">Our Customers</a><a href="#">About Us</a><a href="#">Contact</a>
    </nav>
  </header>

  <h1 class="page-title">Here to help</h1>
  <div class="title-rule"></div>

  <section class="help-panel">
    <p class="help-intro">Lorem Ipsum is simply dummy text of the printing and typesetting industry. Lorem Ipsum has been the industry's standard dummy text ever since the 1500s, when an unknown printer took a galley of type and scrambled it to make a type specimen book. It has survived not only five centuries, but also the leap into electronic typesetting, remaining essentially unchanged.</p>
    <div class="panel-divider"></div>

    <div class="question">
      <h2 class="question-heading">What's your question?</h2>
      <div class="search-form">
        <div class="search-field">
          <svg width="14" height="14" viewBox="0 0 14 14"><circle cx="6" cy="6" r="4.5" fill="none" stroke="#999" stroke-width="1.4"/><line x1="9.3" y1="9.3" x2="13" y2="13" stroke="#999" stroke-width="1.6"/></svg>
          How can we help you...
        </div>
        <div class="search-button">SEARCH</div>
      </div>
    </div>

    <div class="more-help">
      <h2 class="more-help-heading">Need more help?</h2>
      <div class="contact-line">
        <svg width="30" height="22" viewBox="0 0 30 22"><rect x="1" y="2" width="24" height="16" fill="#fff" stroke="#888" stroke-width="1.3"/><polyline points="1,2 13,11 25,2" fill="none" stroke="#888" stroke-width="1.3"/><path d="M18 15h7v-3l5 5-5 5v-3h-7z" fill="#5bb645"/></svg>
        <span><strong>Email us</strong> anytime</span>
      </div>
      <div class="contact-line">
        <svg width="30" height="24" viewBox="0 0 30 24"><path d="M3 9c0-5 24-5 24 0v3h-6v-3h-12v3h-6z" fill="#d33a2c"/><path d="M7 12h16l3 10h-22z" fill="#d33a2c"/><circle cx="15" cy="17" r="3" fill="#fff"/></svg>
        <span><strong>Phone us</strong> Mon-Fri</span>
      </div>
    </div>
  </section>

  <div class="partners-tab">
    <svg width="96" height="20" viewBox="0 0 96 20"><polyline points="42,14 48,8 54,14" fill="none" stroke="#888" stroke-width="2"/></svg>
  </div>
  <h2 class="partners-title">Our Partners:</h2>
  <div class="partners-rule"></div>
  <div class="partner-row" role="img" aria-label="Partner badges">
    <span class="partner-badge" style="left:5px"></span>
    <span class="partner-badge round" style="left:98px"></span>
    <span class="partner-badge" style="left:190px"></span>
    <span class="partner-badge round" style="left:283px"></span>
    <span class="partner-badge round" style="left:376px"></span>
    <span class="partner-badge round" style="left:469px"></span>
    <span class="partner-badge" style="left:560px"></span>
    <span class="partner-badge" style="left:654px"></span>
    <span class="partner-badge round" style="left:732px"></span>
    <span class="partner-badge" style="left:823px"></span>
    <span class="partner-badge round" style="left:900px"></span>
  </div>
  <div class="footer-rule"></div>

  <footer class="site-footer">
    <p>© 2012 RailRoster. All Rights reserved. <a class="terms" href="#">Terms &amp; Conditions</a></p>
    <nav class="footer-nav">
      <a href="#">Home</a><span>-</span><a href="#">How it works</a><span>-</span><a href="#">Prices</a><span>-</span><a href="#">Our Customers</a><span>-</span><a href="#">About us</a><span>-</span><a href="#">Contact</a>
    </nav>
  </footer>
</body>
</html>
```